New business card design needed for Diesel Fitting (Mechanical) Company

We need a new business card for our company called "Gumtree Engine Works" that showcases our logo and business details.
Target Market(s)
Owners of all makes and models of vehicles, trucks, plant and machinery.
Industry/Entity Type
Mechanical
Contact Information for Business Card
The business card details need to include the following: Owners/Directors: Doug & Marisol Brent-Coyle ABN: 41 917 302 846 Address: 317 Wattlebrook Street CHARTERS TOWERS QLD 4820 Postal Address: PO Box 5791 CHARTERS TOWERS QLD 4820 Website: www.gewservice.com.au Phone: 4712 9083 Mobile: 0438 175 906 Emails: sales@gewservice.com.au; admin@gewservice.com.au; accounts@gewservice.com.au; parts@gewservice.com.au; office@gewservice.com.au, reception@gewservice.com.au
Look and feel

```html
<!DOCTYPE html>
<html lang="en">
<head>
<meta charset="utf-8">
<title>Gumtree Engine Works – Business Card</title>
<link rel="stylesheet" href="https://fonts.googleapis.com/css2?family=Figtree:wght@400;500;700;800&display=swap">
<style>
  :root {
    --backdrop: #e4e4e4;
    --card: #ffffff;
    --ink: #1a1a1a;
    --brand-red: #e3232b;
    --brand-orange: #f07522;
  }
  * { box-sizing: border-box; margin: 0; padding: 0; }
  html, body {
    width: 1160px; height: 1200px; overflow: hidden;
    background: var(--backdrop);
    font-family: "Figtree", Arial, sans-serif;
    color: var(--ink);
  }
  .card {
    position: absolute; left: 191px; width: 778px; height: 442px;
    background: var(--card); border-radius: 27px;
    box-shadow: 0 4px 14px rgba(0,0,0,0.12);
  }
  .card--front { top: 104px; }
  .card--back { top: 634px; }

  .brand {
    position: absolute; left: 0; right: 0;
    display: flex; align-items: center; justify-content: center; gap: 12px;
    font-weight: 700; color: var(--brand-orange);
  }
  .brand__dot { border-radius: 50%; background: var(--brand-red); flex: none; }
  .card--front .brand { top: 98px; font-size: 30px; }
  .card--front .brand__dot { width: 26px; height: 26px; }
  .card--back .brand { top: 184px; font-size: 44px; }
  .card--back .brand__dot { width: 38px; height: 38px; }

  .owners {
    position: absolute; top: 212px; left: 0; right: 0; text-align: center;
    font-weight: 800; font-size: 23px; color: var(--brand-red); letter-spacing: 0.2px;
  }
  .role {
    position: absolute; top: 243px; left: 0; right: 0; text-align: center;
    font-weight: 500; font-size: 20px;
  }
  .divider {
    position: absolute; top: 276px; left: 83px; width: 587px; height: 2px;
    background: linear-gradient(90deg, rgba(227,35,43,0.4), var(--brand-red) 15%, var(--brand-red) 85%, rgba(227,35,43,0.4));
  }
  .contacts { position: absolute; top: 292px; left: 85px; }
  .contacts__row {
    display: flex; align-items: center; height: 30.5px;
    font-size: 19px; font-weight: 500; white-space: nowrap;
  }
  .contacts__item { display: flex; align-items: center; margin-right: 8px; }
  .contacts__item svg { flex: none; margin-right: 9px; }
  .contacts__row > .contacts__item:first-child svg { margin-right: 20px; }

  .abn {
    position: absolute; left: 733px; top: 222px;
    transform: translate(-50%, -50%) rotate(-90deg);
    font-size: 19px; font-weight: 500; white-space: nowrap; letter-spacing: 0.4px;
  }
  .abn__label { color: var(--brand-red); }

  .address {
    position: absolute; top: 352px; left: 0; right: 0; text-align: center;
    font-size: 19.5px; font-weight: 500; line-height: 32px;
  }
</style>
</head>
<body>

<section class="card card--front">
  <div class="brand"><span class="brand__dot"></span>Gumtree Engine Works</div>
  <h1 class="owners">DOUG &amp; MARISOL BRENT-COYLE</h1>
  <p class="role">Owners/Directors</p>
  <div class="divider"></div>

  <div class="contacts">
    <div class="contacts__row">
      <span class="contacts__item">
        <svg width="22" height="20" viewBox="0 0 24 22" fill="var(--brand-red)"><path d="M5 2l4 4-2 3c1.5 3 3.5 5 6.5 6.5l3-2 4 4-3 3C10 20 3 12 2 5z"/><path d="M13 2a8 8 0 0 1 8 8h-2a6 6 0 0 0-6-6zM13 6a4 4 0 0 1 4 4h-2a2 2 0 0 0-2-2z"/></svg>
        4712 9083
      </span>
      <span class="contacts__item">
        <svg width="14" height="22" viewBox="0 0 14 22" fill="none" stroke="var(--brand-red)" stroke-width="2"><rect x="1.5" y="1" width="11" height="20" rx="2"/><circle cx="7" cy="17.5" r="1" fill="var(--brand-red)"/></svg>
        0438 175 906
      </span>
      <span class="contacts__item">
        <svg width="21" height="14" viewBox="0 0 21 14"><rect width="21" height="14" fill="var(--brand-red)"/><path d="M0 0l10.5 8L21 0M0 14l7-6M21 14l-7-6" stroke="#fff" stroke-width="1.5" fill="none"/></svg>
        sales@gewservice.com.au
      </span>
    </div>
    <div class="contacts__row">
      <span class="contacts__item">
        <svg width="21" height="14" viewBox="0 0 21 14"><rect width="21" height="14" fill="var(--brand-red)"/><path d="M0 0l10.5 8L21 0M0 14l7-6M21 14l-7-6" stroke="#fff" stroke-width="1.5" fill="none"/></svg>
        admin@gewservice.com.au
      </span>
      <span class="contacts__item">
        <svg width="21" height="14" viewBox="0 0 21 14"><rect width="21" height="14" fill="var(--brand-red)"/><path d="M0 0l10.5 8L21 0M0 14l7-6M21 14l-7-6" stroke="#fff" stroke-width="1.5" fill="none"/></svg>
        accounts@gewservice.com.au
      </span>
    </div>
    <div class="contacts__row">
      <span class="contacts__item">
        <svg width="21" height="14" viewBox="0 0 21 14"><rect width="21" height="14" fill="var(--brand-red)"/><path d="M0 0l10.5 8L21 0M0 14l7-6M21 14l-7-6" stroke="#fff" stroke-width="1.5" fill="none"/></svg>
        parts@gewservice.com.au
      </span>
      <span class="contacts__item">
        <svg width="21" height="14" viewBox="0 0 21 14"><rect width="21" height="14" fill="var(--brand-red)"/><path d="M0 0l10.5 8L21 0M0 14l7-6M21 14l-7-6" stroke="#fff" stroke-width="1.5" fill="none"/></svg>
        office@gewservice.com.au
      </span>
    </div>
    <div class="contacts__row">
      <span class="contacts__item">
        <svg width="21" height="14" viewBox="0 0 21 14"><rect width="21" height="14" fill="var(--brand-red)"/><path d="M0 0l10.5 8L21 0M0 14l7-6M21 14l-7-6" stroke="#fff" stroke-width="1.5" fill="none"/></svg>
        reception@gewservice.com.au
      </span>
      <span class="contacts__item">
        <svg width="20" height="20" viewBox="0 0 20 20"><circle cx="10" cy="10" r="9.5" fill="var(--brand-red)"/><path d="M4 6c2 0 3 1 3 3s2 2 2 4-1 3-2 4M12 3c0 2 2 3 4 3M13 11c1 0 3 1 3 3" stroke="#fff" stroke-width="1.4" fill="none"/></svg>
        www.gewservice.com.au
      </span>
    </div>
  </div>

  <p class="abn"><span class="abn__label">ABN:</span> 41 917 302 846</p>
</section>

<section class="card card--back">
  <div class="brand"><span class="brand__dot"></span>Gumtree Engine Works</div>
  <address class="address" style="font-style: normal;">
    317 Wattlebrook Street CHARTERS TOWERS QLD 4820 Postal<br>
    PO Box 5791 CHARTERS TOWERS QLD 4820
  </address>
</section>

</body>
</html>
```